Lets get creative with Pelloway Finance Brochure

I have used artfolkhub before for a previous brochure which is attached business BRAMLE Automotive. I would like to work together on a new project PELLOWAY Finance. https://pellowayfinance.com.au/
It is a boutique Finance company ideally targeting the small to Medium business s along with consumer finance. I have attached previous brochure to give an idea of layout. Once we have a layout i will send wording through.

Target Market(s)

business owners

Industry/Entity Type

Finance

Font styles to use
Serif

Colors
0355a3
fef3ec

```html
<!DOCTYPE html>
<html lang="en">
<head>
<meta charset="utf-8">
<title>Pelloway Finance – Brochure</title>
<link rel="stylesheet" href="https://fonts.googleapis.com/css2?family=Playfair+Display:wght@400;600;700&family=Lora:wght@400;500;600&display=swap">
<style>
  :root {
    --brand-blue: #0355a3;
    --cream: #fef3ec;
    --ink: #1b1f26;
    --white: #ffffff;
    --rule: rgba(255,255,255,0.75);
    --serif-display: "Playfair Display", serif;
    --serif-text: "Lora", serif;
  }
  html, body { margin: 0; padding: 0; overflow: hidden; background: var(--cream); }
  .brochure {
    position: relative; width: 1200px; height: 927px; overflow: hidden;
    background: var(--cream); font-family: var(--serif-text); color: var(--ink);
  }
  .shape { position: absolute; left: 0; top: 0; }

  .about-photo {
    position: absolute; left: 104px; top: 45px; width: 196px; height: 196px; border-radius: 50%;
    background: radial-gradient(circle at 40% 45%, #f6f6f4 0%, #e4e5e3 55%, #c9cbc8 100%);
  }
  .section-title {
    position: absolute; margin: 0; font-family: var(--serif-display); font-weight: 400;
    text-align: center; letter-spacing: 0.5px; line-height: 1; white-space: nowrap;
  }
  .about-title { left: 0; width: 400px; top: 270px; font-size: 35px; color: var(--white); }
  .why-title { left: 0; width: 410px; top: 582px; font-size: 35px; color: var(--brand-blue); }
  .body-copy {
    position: absolute; margin: 0; font-weight: 400; font-size: 16.5px; line-height: 24.2px;
    text-align: center; white-space: nowrap;
  }
  .about-copy { left: 0; width: 400px; top: 313px; color: var(--white); }
  .why-copy { left: 0; width: 410px; top: 626px; color: var(--ink); }

  .brand-mark { position: absolute; margin: 0; font-family: var(--serif-display); font-weight: 600; text-align: center; line-height: 1; }
  .brand-mark .word { display: block; }
  .brand-mark .sub { display: block; font-family: var(--serif-text); font-weight: 500; }
  .brand-mark--cover { left: 428px; width: 340px; top: 290px; color: var(--white); }
  .brand-mark--cover .word { font-size: 40px; letter-spacing: 6px; }
  .brand-mark--cover .sub { font-size: 16px; letter-spacing: 18px; margin-top: 18px; padding-left: 18px; }
  .brand-mark--front { left: 836px; width: 320px; top: 56px; color: var(--brand-blue); }
  .brand-mark--front .word { font-size: 38px; letter-spacing: 6px; }
  .brand-mark--front .sub { font-size: 16px; letter-spacing: 18px; margin-top: 16px; padding-left: 18px; }

  .front-headline {
    position: absolute; left: 841px; top: 180px; width: 350px; margin: 0;
    font-weight: 500; font-size: 22.5px; line-height: 34px; color: var(--ink); white-space: nowrap;
  }

  .contact { position: absolute; left: 455px; top: 522px; width: 330px; color: var(--white); }
  .contact h2 { margin: 0; font-family: var(--serif-display); font-weight: 700; font-size: 42px; line-height: 48px; white-space: nowrap; }
  .contact p { margin: 0; font-weight: 400; font-size: 16.5px; line-height: 24px; }
  .contact h3 { margin: 16px 0 4px; font-weight: 600; font-size: 17px; letter-spacing: 0.3px; }
  .contact .web {
    margin-top: 14px; width: 281px; border-top: 1px solid var(--rule); border-bottom: 1px solid var(--rule);
    padding: 6px 0 7px;
  }
  .contact .phone { margin: 20px 0 0; font-family: var(--serif-display); font-weight: 700; font-size: 30px; line-height: 36px; white-space: nowrap; }
</style>
</head>
<body>
<main class="brochure">
  <svg class="shape" width="1200" height="927" aria-hidden="true">
    <polygon points="0,0 400,0 400,459 0,542" fill="var(--brand-blue)"/>
    <polygon points="400,451 800,380 800,927 400,927" fill="var(--brand-blue)"/>
  </svg>

  <svg class="shape" width="1200" height="927" role="img" aria-label="Photo of hands using a tablet and stylus at a desk">
    <defs>
      <linearGradient id="tabletTone" x1="0" y1="0" x2="1" y2="1">
        <stop offset="0" stop-color="#8fb4c8"/>
        <stop offset="0.5" stop-color="#4f6f86"/>
        <stop offset="1" stop-color="#2b3f5a"/>
      </linearGradient>
    </defs>
    <polygon points="400,0 800,0 800,380 400,451" fill="url(#tabletTone)"/>
  </svg>

  <svg class="shape" width="1200" height="927" role="img" aria-label="Photo of a cup of coffee beside printed financial charts on a wooden table">
    <defs>
      <linearGradient id="coffeeTone" x1="0" y1="0" x2="1" y2="1">
        <stop offset="0" stop-color="#a8764a"/>
        <stop offset="0.45" stop-color="#c9a27a"/>
        <stop offset="0.75" stop-color="#dfe0d8"/>
        <stop offset="1" stop-color="#9cc93e"/>
      </linearGradient>
    </defs>
    <polygon points="800,380 1200,298 1200,927 800,927" fill="url(#coffeeTone)"/>
  </svg>

  <div class="about-photo" role="img" aria-label="Photo of a calculator, coins and a piggy bank"></div>

  <h2 class="section-title about-title">ABOUT US</h2>
  <p class="body-copy about-copy">Lorem ipsum dolor sit amet,<br>consectetur adipiscing elit, sed do<br>eiusmod tempor incididunt ut<br>labore et dolore magna aliqua. Ut<br>enim ad minim veniam, quis<br>nostrud exercitation</p>

  <h2 class="section-title why-title">WHY CHOOSE US</h2>
  <p class="body-copy why-copy">Lorem ipsum dolor sit amet,<br>consectetur adipiscing elit, sed do<br>eiusmod tempor incididunt ut<br>labore et dolore magna aliqua. Ut<br>enim ad minim veniam, quis<br>nostrud exercitation ullamco<br>laboris nisi ut aliquip ex ea<br>commodo consequat. Duis aute<br>irure dolor in reprehenderit</p>

  <p class="brand-mark brand-mark--cover"><span class="word">PELLOWAY</span><span class="sub">FINANCE</span></p>

  <section class="contact">
    <h2>CONTACT US</h2>
    <p>14 Marlow Lane</p>
    <p>Kelvinhurst, QLD 4012</p>
    <h3>HOURS OF OPERATION</h3>
    <p>MON - FRI: 8:30am - 5:30pm</p>
    <p>SAT: 8:30am - 12noon</p>
    <p class="web">Loremipsumdolor.com</p>
    <p class="phone">PH: 07 3000 5187</p>
  </section>

  <p class="brand-mark brand-mark--front"><span class="word">PELLOWAY</span><span class="sub">FINANCE</span></p>
  <h1 class="front-headline">LOREM IPSUM DOLOR<br>SIT AMET, CONSECTETUR<br>ADIPISCING ELI</h1>
</main>
</body>
</html>
```